Diagramm/Grafik zur Darstellung einer Formel
Zielgruppe
Das Unternehmen ist in der Unternehmensberatung tätig und beschäftigt sich mit der Analyse von IT-In- und Outsourcing.
Zielgruppe: Entscheider / Höheres Management / Round Table
Aufgabenstellung
Es wurde für die Bewertung des bestehenden Outsourcing eine Formel entwickelt, welche es ermöglicht einerseits die Stärken
und Schwächen und andererseits die Entwicklung und Vorteilhaftigkeit der Kosten für die nächsten Jahre zu prognostizieren.
Der Name der Formel ist "MIRAX-P Methode" (Strategie, Technologie, Organisation, Qualität und Kosten)
Die Formel ist aufgebaut aus 5 Sektoren, unter welchem jeweils 3-8 Faktoren untergeordnet sind. (siehe IMG_1159)
Die Zuordnung der Faktoren zu Sektoren (siehe SektorenFaktoren.pdf) ist variabel, aus welchem Grund unter jedem Sektor 3-8 Faktoren unterordnenbar sein sollten.
Grundsätzlich findet die Auswertung aus dem Vergleich von Kosten + Risiken - Chancen jeweils von Outsourcing und Insourcing statt. (siehe IMG_1190)
Ziel ist es, eine Darstellung der Sektoren und Faktoren sowie der Formel zu finden, welche:
a) die Abhängigkeit von den Faktoren zu den Sektoren darstellt
b) die Formel darstellt
c) sich als Ganzes oder in Teilen für diverse Unterlagen verwenden lässt (bspw. .pptx, .pdf, etc.)
--> es ist geplant diese Darstellung bspw. als Ganzes oder in Teilen in eine PowerPoint-Präsentation zu integrieren
Diese Aufgabenstellung ist ein erster Versuch mittels der Plattform pixelhafen.de Aufträge zu vergeben.
Bei Erfolg sind Anschlussaufträge geplant.
WICHTIG: Alle Anhänge diesen lediglich zur Darstellung der Zusammenhänge, sollen aber keinerlei design vorgeben!

```html
<!DOCTYPE html>
<html lang="de">
<head>
<meta charset="utf-8">
<title>MIRAX-P Methode – Formeldarstellung</title>
<link rel="stylesheet" href="https://fonts.googleapis.com/css2?family=Barlow:wght@400;500;600;700&family=Barlow+Semi+Condensed:wght@500;600;700&display=swap">
<style>
  :root {
    --blue: #5a7b9f;
    --blue-dark: #4f6f93;
    --orange: #e2571c;
    --grey: #5b5b5b;
    --white: #ffffff;
    --dot: #8fa6c0;
  }
  * { margin: 0; padding: 0; box-sizing: border-box; }
  html, body { width: 1200px; height: 900px; overflow: hidden; background: var(--white); }
  body { font-family: "Barlow", Arial, sans-serif; color: var(--grey); }
  .canvas { position: relative; width: 1200px; height: 900px; overflow: hidden; }

  .title-band {
    position: absolute; left: 0; top: 0; width: 1200px; height: 66px;
    background: var(--blue); border-bottom: 4px solid #7c98b8;
    display: flex; align-items: center; justify-content: center;
  }
  .title-band h1 {
    color: var(--white); font-family: "Barlow Semi Condensed", sans-serif;
    font-weight: 600; font-size: 38px; letter-spacing: 9px;
  }
  .foot-band { position: absolute; left: 0; bottom: 0; width: 1200px; height: 12px; background: var(--blue); }

  .graphics { position: absolute; left: 0; top: 0; }

  .side-title {
    position: absolute; top: 108px; width: 420px; text-align: center;
    color: var(--orange); font-family: "Barlow Semi Condensed", sans-serif;
    font-weight: 700; font-size: 34px; letter-spacing: 5px;
  }
  .side-title.out { left: 112px; }
  .side-title.in { left: 718px; }

  .formula {
    position: absolute; top: 238px; width: 470px; text-align: center;
    font-family: "Barlow", sans-serif; font-weight: 500; font-size: 29px;
    letter-spacing: 3.5px; color: var(--grey); white-space: nowrap;
  }
  .formula.out { left: 70px; }
  .formula.in { left: 680px; }
  .formula .paren { color: var(--blue); }

  .sector { position: absolute; width: 150px; }
  .sector .head { display: flex; align-items: flex-end; gap: 4px; height: 34px; }
  .sector .icon { width: 34px; height: 34px; flex: none; }
  .sector h3 {
    font-family: "Barlow", sans-serif; font-weight: 500; font-size: 13.5px;
    color: var(--blue); text-transform: uppercase; line-height: 1; margin-bottom: 6px;
  }
  .sector ol {
    list-style: none; margin: 2px 0 0 49px; counter-reset: f;
    font-size: 12.5px; font-weight: 500; color: var(--blue); line-height: 18.5px;
  }
  .sector ol li { counter-increment: f; }
  .sector ol li::before { content: counter(f) "."; }
  .sector.cost h3, .sector.cost ol { color: var(--orange); }

  .note {
    position: absolute; left: 0; top: 846px; width: 1200px; text-align: center;
    color: var(--orange); font-size: 22px; font-weight: 500;
  }
</style>
</head>
<body>
<div class="canvas">
  <header class="title-band"><h1>MIRAX-P</h1></header>

  <svg class="graphics" width="1200" height="900" viewBox="0 0 1200 900" aria-hidden="true">
    <!-- centre divider -->
    <line x1="600" y1="96" x2="600" y2="815" stroke="var(--dot)" stroke-width="3" stroke-dasharray="1 8" stroke-linecap="round"/>
    <polyline points="592,808 600,818 608,808" fill="none" stroke="var(--blue)" stroke-width="2.5"/>
    <!-- comparison symbol -->
    <rect x="571" y="232" width="58" height="56" fill="var(--white)" stroke="var(--dot)" stroke-width="2.5" stroke-dasharray="1 6" stroke-linecap="round"/>
    <g fill="none" stroke="var(--blue)" stroke-width="2.5">
      <polyline points="586,248 614,256 586,264"/>
      <polyline points="614,258 586,266 614,274"/>
      <line x1="586" y1="270" x2="614" y2="270"/>
      <line x1="586" y1="252" x2="614" y2="252" opacity="0"/>
    </g>

    <!-- braces -->
    <g fill="none" stroke-width="6" stroke-linecap="round">
      <path stroke="var(--orange)" d="M105,220 C105,185 115,182 160,182 L290,182 C315,182 318,176 322,160 C326,176 329,182 354,182 L455,182 C488,182 494,188 494,220"/>
      <path stroke="var(--orange)" d="M728,220 C728,185 738,182 780,182 L895,182 C920,182 923,176 927,160 C931,176 934,182 959,182 L1070,182 C1104,182 1110,188 1110,220"/>
      <path stroke="var(--blue)" stroke-width="5" d="M218,285 C218,310 224,314 260,314 L330,314 C350,314 354,318 357,334 C360,318 364,314 384,314 L460,314 C490,314 495,310 495,285"/>
      <path stroke="var(--blue)" stroke-width="5" d="M818,285 C818,310 824,314 860,314 L930,314 C950,314 954,318 957,334 C960,318 964,314 984,314 L1072,314 C1104,314 1110,310 1110,285"/>
    </g>

    <!-- dotted arrows -->
    <g fill="none" stroke-width="3" stroke-linecap="round">
      <line x1="112" y1="290" x2="112" y2="395" stroke="var(--orange)" stroke-dasharray="1 7"/>
      <polyline points="104,390 112,400 120,390" stroke="var(--orange)" stroke-width="2.5"/>
      <line x1="357" y1="340" x2="357" y2="395" stroke="var(--blue)" stroke-dasharray="1 7"/>
      <polyline points="349,390 357,400 365,390" stroke="var(--blue)" stroke-width="2.5"/>
      <line x1="708" y1="290" x2="708" y2="395" stroke="var(--orange)" stroke-dasharray="1 7"/>
      <polyline points="700,390 708,400 716,390" stroke="var(--orange)" stroke-width="2.5"/>
      <line x1="960" y1="340" x2="960" y2="395" stroke="var(--blue)" stroke-dasharray="1 7"/>
      <polyline points="952,390 960,400 968,390" stroke="var(--blue)" stroke-width="2.5"/>
    </g>

    <!-- icon symbols -->
    <defs>
      <g id="icon-cost">
        <rect x="0" y="0" width="34" height="34" fill="var(--orange)"/>
        <rect x="6" y="6" width="22" height="22" fill="var(--white)"/>
        <rect x="22" y="12" width="8" height="10" fill="var(--orange)" stroke="var(--white)" stroke-width="2"/>
      </g>
      <g id="icon-strategy">
        <rect x="0" y="0" width="34" height="34" fill="var(--blue)"/>
        <line x1="8" y1="27" x2="22" y2="13" stroke="var(--white)" stroke-width="3"/>
        <path d="M24,5 l1.5,3.5 3.5,1.5 -3.5,1.5 -1.5,3.5 -1.5,-3.5 -3.5,-1.5 3.5,-1.5z" fill="var(--white)"/>
        <circle cx="13" cy="9" r="1.5" fill="var(--white)"/>
        <circle cx="27" cy="20" r="1.5" fill="var(--white)"/>
      </g>
      <g id="icon-tech">
        <rect x="0" y="0" width="34" height="34" fill="var(--blue)"/>
        <circle cx="12" cy="21" r="6" fill="none" stroke="var(--white)" stroke-width="4" stroke-dasharray="2.5 1.7"/>
        <circle cx="12" cy="21" r="2" fill="var(--white)"/>
        <circle cx="23" cy="11" r="4.5" fill="none" stroke="var(--white)" stroke-width="3.5" stroke-dasharray="2 1.5"/>
      </g>
      <g id="icon-org">
        <rect x="0" y="0" width="34" height="34" fill="var(--blue)"/>
        <rect x="7" y="8" width="20" height="19" fill="none" stroke="var(--white)" stroke-width="2.5"/>
        <line x1="17" y1="8" x2="17" y2="27" stroke="var(--white)" stroke-width="2"/>
        <rect x="9" y="10" width="6" height="15" fill="var(--white)"/>
      </g>
      <g id="icon-quality">
        <rect x="0" y="0" width="34" height="34" fill="var(--blue)"/>
        <circle cx="19" cy="14" r="7" fill="none" stroke="var(--white)" stroke-width="3"/>
        <line x1="14" y1="19" x2="7" y2="27" stroke="var(--white)" stroke-width="4" stroke-linecap="round"/>
      </g>
    </defs>
    <use href="#icon-cost" x="22" y="461"/>
    <use href="#icon-strategy" x="207" y="461"/>
    <use href="#icon-tech" x="401" y="461"/>
    <use href="#icon-org" x="207" y="648"/>
    <use href="#icon-quality" x="401" y="648"/>
    <use href="#icon-cost" x="624" y="454"/>
    <use href="#icon-strategy" x="809" y="454"/>
    <use href="#icon-tech" x="1003" y="454"/>
    <use href="#icon-org" x="809" y="648"/>
    <use href="#icon-quality" x="1003" y="648"/>
  </svg>

  <h2 class="side-title out">OUTSOURCING*</h2>
  <h2 class="side-title in">INSOURCING*</h2>

  <p class="formula out">OS + <span class="paren">(</span>Chancen - Risiken<span class="paren">)</span></p>
  <p class="formula in">IS + <span class="paren">(</span>Chancen - Risiken<span class="paren">)</span></p>

  <!-- Outsourcing sectors -->
  <section class="sector cost" style="left:22px;top:461px"><div class="head"><span class="icon"></span><h3>Kosten</h3></div><ol><li></li><li></li><li></li><li></li><li></li><li></li><li></li><li></li></ol></section>
  <section class="sector" style="left:207px;top:461px"><div class="head"><span class="icon"></span><h3>Strategie</h3></div><ol><li></li><li></li><li></li><li></li><li></li><li></li><li></li><li></li></ol></section>
  <section class="sector" style="left:401px;top:461px"><div class="head"><span class="icon"></span><h3>Technologie</h3></div><ol><li></li><li></li><li></li><li></li><li></li><li></li><li></li><li></li></ol></section>
  <section class="sector" style="left:207px;top:648px"><div class="head"><span class="icon"></span><h3>Organisation</h3></div><ol><li></li><li></li><li></li><li></li><li></li><li></li><li></li><li></li></ol></section>
  <section class="sector" style="left:401px;top:648px"><div class="head"><span class="icon"></span><h3>Qualität</h3></div><ol><li></li><li></li><li></li><li></li><li></li><li></li><li></li><li></li></ol></section>

  <!-- Insourcing sectors -->
  <section class="sector cost" style="left:624px;top:454px"><div class="head"><span class="icon"></span><h3>Kosten</h3></div><ol><li></li><li></li><li></li><li></li><li></li><li></li><li></li><li></li></ol></section>
  <section class="sector" style="left:809px;top:454px"><div class="head"><span class="icon"></span><h3>Strategie</h3></div><ol><li></li><li></li><li></li><li></li><li></li><li></li><li></li><li></li></ol></section>
  <section class="sector" style="left:1003px;top:454px"><div class="head"><span class="icon"></span><h3>Technologie</h3></div><ol><li></li><li></li><li></li><li></li><li></li><li></li><li></li><li></li></ol></section>
  <section class="sector" style="left:809px;top:648px"><div class="head"><span class="icon"></span><h3>Organisation</h3></div><ol><li></li><li></li><li></li><li></li><li></li><li></li><li></li><li></li></ol></section>
  <section class="sector" style="left:1003px;top:648px"><div class="head"><span class="icon"></span><h3>Qualität</h3></div><ol><li></li><li></li><li></li><li></li><li></li><li></li><li></li><li></li></ol></section>

  <p class="note">*Vergleich der Nutzen v. Is / Os</p>
  <div class="foot-band"></div>
</div>
</body>
</html>
```